New Meal Prep Flyer for New Package Deals

We are looking for a design that displays our new packages that we offer. If you take a look at our website www.brambleforkmeals.com, and click on packages , you'll see the way we display them currently . We would like something similar to that in style . The first package is called "Horizon" and this package will be a 1 week package (7 days ), 2 meals a day, for a price of $195.00. The second package is called "Amber" and this package will be a 3 week package (21 days) 2 meals per day, for a price of $546.00 , the third package is a 6 week+ package (45 days), and it is called "Evergreen" , 2 meals per day , and the price is $1080.00 .
For the Amber Package , can you put next to it "Save $42.00!"
For the Evergreen Package, can you put next to it "Save $180!"
We also want our logo on the flyer (see attached), and we are just looking for a 1 page flyer , 8 1/2 x 11.

```html
<!DOCTYPE html>
<html lang="en">
<head>
<meta charset="utf-8">
<title>Bramble Fork Kitchen – Meal Prep Packages</title>
<link rel="stylesheet" href="https://fonts.googleapis.com/css2?family=Archivo+Black&family=Kanit:ital,wght@1,700&family=Montserrat:wght@800&display=swap">
<style>
  :root{
    --green-light:#8cc63f;
    --green-dark:#3f8a37;
    --green-brand:#7dc242;
    --charcoal:#3a3a3a;
    --gray-top:#6d6d6d;
    --gray-bottom:#c9c9c9;
    --ink:#111;
    --white:#fff;
    --photo-a:#2f3a28;
    --photo-b:#5b3e2a;
    --photo-c:#7a4a30;
  }
  *{box-sizing:border-box;margin:0;padding:0}
  html,body{width:1200px;height:1019px;overflow:hidden;background:#d4d4d4}
  .flyer{position:relative;width:1200px;height:1019px;overflow:hidden}
  .food-photo{position:absolute;inset:0;
    background:radial-gradient(ellipse at 85% 65%,var(--photo-c) 0%,transparent 45%),
               radial-gradient(ellipse at 15% 35%,var(--photo-b) 0%,transparent 40%),
               linear-gradient(160deg,#1f2a1c 0%,var(--photo-a) 45%,#3b3a2c 100%)}
  .backdrop{position:absolute;inset:0}
  .brand{position:absolute;top:48px;left:0;right:0;text-align:center}
  .brand-name{font-family:"Montserrat",sans-serif;font-weight:800;font-size:112px;letter-spacing:4px;color:var(--white);line-height:1}
  .brand-tagline{margin-top:14px;font-family:"Montserrat",sans-serif;font-weight:800;font-size:40px;letter-spacing:1px;color:var(--green-brand)}
  .packages{position:absolute;top:310px;left:80px;right:80px;display:flex;justify-content:space-between}
  .package{position:relative;width:320px;height:600px;border:5px solid var(--white);border-radius:48px 48px 48px 48px;
    background:linear-gradient(135deg,var(--green-light) 0%,var(--green-dark) 100%);
    box-shadow:0 6px 14px rgba(0,0,0,.35)}
  .package-name{position:absolute;top:-26px;left:40px;right:18px;height:92px;border:5px solid var(--white);border-radius:30px;
    background:linear-gradient(#555,var(--charcoal));color:var(--white);font-family:"Archivo Black",sans-serif;font-size:40px;
    display:flex;align-items:center;justify-content:center}
  .package-price{position:absolute;top:100px;left:-5px;width:330px;height:84px;background:var(--white);
    clip-path:polygon(0 0,100% 0,82% 100%,0 100%);font-family:"Archivo Black",sans-serif;font-size:48px;color:var(--ink);
    display:flex;align-items:center;padding-left:30px}
  .features{position:absolute;top:222px;left:30px;right:16px;list-style:none}
  .feature{display:flex;align-items:flex-start;gap:14px;margin-bottom:30px;font-family:"Kanit",sans-serif;font-style:italic;
    font-weight:700;font-size:34px;line-height:.95;color:#1e2a1a}
  .feature svg{flex:none;width:50px;height:42px;margin-top:2px}
  .saving{position:absolute;left:36px;right:-5px;bottom:-5px;height:86px;background:var(--white);border-radius:40px 0 44px 0;
    display:flex;align-items:center;justify-content:center;gap:10px;font-family:"Kanit",sans-serif;font-style:italic;font-weight:700;color:var(--ink)}
  .saving small{font-size:24px}
  .saving strong{font-size:44px}
</style>
</head>
<body>
<main class="flyer">
  <div class="food-photo" role="img" aria-label="Photograph of prepared healthy meals with grains, greens and shrimp"></div>
  <svg class="backdrop" viewBox="0 0 1200 1019" preserveAspectRatio="none" aria-hidden="true">
    <defs>
      <linearGradient id="grayFade" x1="0" y1="0" x2="0" y2="1">
        <stop offset="0" stop-color="var(--gray-top)"/>
        <stop offset="1" stop-color="var(--gray-bottom)"/>
      </linearGradient>
    </defs>
    <path d="M0 330 Q420 520 760 760 Q980 900 1200 860 L1200 1019 L0 1019Z" fill="var(--green-brand)"/>
    <path d="M0 352 Q420 545 760 785 Q980 925 1200 885 L1200 1019 L0 1019Z" fill="var(--white)"/>
    <path d="M0 380 Q420 570 760 810 Q980 950 1200 910 L1200 1019 L0 1019Z" fill="url(#grayFade)"/>
    <path d="M0 380 L0 1019 L1200 1019 L1200 980 Q700 1000 300 600 Q150 450 0 380Z" fill="url(#grayFade)"/>
  </svg>

  <header class="brand">
    <h1 class="brand-name">BRAMBLE FORK</h1>
    <p class="brand-tagline">HEALTHY KITCHEN | MEAL PREP</p>
  </header>

  <section class="packages">
    <article class="package">
      <h2 class="package-name">Horizon</h2>
      <p class="package-price">$195.00</p>
      <ul class="features">
        <li class="feature"><svg viewBox="0 0 50 42"><circle cx="20" cy="22" r="16" fill="none" stroke="#1e2a1a" stroke-width="4"/><path d="M11 21l8 8L46 4" fill="none" stroke="#1e2a1a" stroke-width="6" stroke-linecap="round" stroke-linejoin="round"/></svg><span>1 week<br>package</span></li>
        <li class="feature"><svg viewBox="0 0 50 42"><circle cx="20" cy="22" r="16" fill="none" stroke="#1e2a1a" stroke-width="4"/><path d="M11 21l8 8L46 4" fill="none" stroke="#1e2a1a" stroke-width="6" stroke-linecap="round" stroke-linejoin="round"/></svg><span>2 meals<br>per day</span></li>
      </ul>
    </article>

    <article class="package">
      <h2 class="package-name">Amber</h2>
      <p class="package-price">$546.00</p>
      <ul class="features">
        <li class="feature"><svg viewBox="0 0 50 42"><circle cx="20" cy="22" r="16" fill="none" stroke="#1e2a1a" stroke-width="4"/><path d="M11 21l8 8L46 4" fill="none" stroke="#1e2a1a" stroke-width="6" stroke-linecap="round" stroke-linejoin="round"/></svg><span>3 week<br>package</span></li>
        <li class="feature"><svg viewBox="0 0 50 42"><circle cx="20" cy="22" r="16" fill="none" stroke="#1e2a1a" stroke-width="4"/><path d="M11 21l8 8L46 4" fill="none" stroke="#1e2a1a" stroke-width="6" stroke-linecap="round" stroke-linejoin="round"/></svg><span>2 meals<br>per day</span></li>
      </ul>
      <p class="saving"><small>Save</small><strong>$42!</strong></p>
    </article>

    <article class="package">
      <h2 class="package-name">Evergreen</h2>
      <p class="package-price">$1080.00</p>
      <ul class="features">
        <li class="feature"><svg viewBox="0 0 50 42"><circle cx="20" cy="22" r="16" fill="none" stroke="#1e2a1a" stroke-width="4"/><path d="M11 21l8 8L46 4" fill="none" stroke="#1e2a1a" stroke-width="6" stroke-linecap="round" stroke-linejoin="round"/></svg><span>6 week+<br>package</span></li>
        <li class="feature"><svg viewBox="0 0 50 42"><circle cx="20" cy="22" r="16" fill="none" stroke="#1e2a1a" stroke-width="4"/><path d="M11 21l8 8L46 4" fill="none" stroke="#1e2a1a" stroke-width="6" stroke-linecap="round" stroke-linejoin="round"/></svg><span>2 meals<br>per day</span></li>
      </ul>
      <p class="saving"><small>Save</small><strong>$180!</strong></p>
    </article>
  </section>
</main>
</body>
</html>
```